Fernwick Digital Marketing Agency Website Design. I need a new website for my digital marketing agency. It needs to be FAST and easy to use. I want to be able to add videos to the main homepage like this page: https://www.lumatreeweb.example/search-marketing/cleveland-ohio-seo-companyI'd like to have the request quote tab on the top right side as well as my number above it. The following website is my favorite overall: http://www.vantorelgroup.example/ I'd love to copy something like that.

***** Website I want to copy: http://www.vantorelgroup.example/services/ ******
Updates

This needs to be a Wordpress website. Sorry for any confusion as this is the first time using MakerQuill. I need the homepage as described as well as a Services Page and Contact Us page. Services page should be simply yet creative with a spot for me to insert up to 8 services.

Target Market(s)

Business owners

Industry/Entity Type

Digital Marketing

Coding

Coded - Design and coding required

Number of Pages Required

3 page

Font styles to use
Other font styles liked:
• Oswald

Colors

Designer to choose colors to be used in the design.

Requirements
Must have
• I need to have a nice design/template to work off of in Wordpress. It needs to be bright and vibrant yet elegant in design.
Nice to have
• CTA at the top right as well as a place for the phone number. http://www.vantorelgroup.example/services/

```html
<!DOCTYPE html>
<html lang="en">
<head>
<meta charset="utf-8">
<title>Fernwick Digital Marketing Agency</title>
<link rel="stylesheet" href="https://fonts.googleapis.com/css2?family=Oswald:wght@300;400;500;600;700&family=Roboto:wght@400;500;700&display=swap">
<style>
:root{
  --blue:#3b5aa8;
  --blue-deep:#2c4690;
  --blue-soft:#5670b6;
  --orange:#ff6a00;
  --ink:#1b1b24;
  --text:#55585f;
  --line:#e6e8ee;
  --ghost:#f1f2f5;
  --white:#ffffff;
}
*{box-sizing:border-box;margin:0;padding:0}
html,body{width:1200px;height:2875px;overflow:hidden;background:var(--white)}
body{position:relative;font-family:"Roboto",Arial,sans-serif;color:var(--ink)}
.abs{position:absolute}
.oswald{font-family:"Oswald","Arial Narrow",sans-serif}
.btn{position:absolute;display:flex;align-items:center;justify-content:center;background:var(--orange);color:var(--white);font-family:"Oswald",sans-serif;font-weight:500;border-radius:3px;text-transform:uppercase;box-shadow:0 4px 10px rgba(255,106,0,.25)}

/* hero */
.hero{position:absolute;left:0;top:0;width:1200px;height:515px;background:linear-gradient(120deg,#2d4a94 0%,#3d5aa6 55%,#4b64ad 100%);overflow:hidden}
.hero-cut{position:absolute;left:0;top:0}
.logo{position:absolute;left:134px;top:34px;display:flex;align-items:center;gap:14px;color:var(--white);font-family:"Oswald",sans-serif;font-weight:600;font-size:19px;letter-spacing:.3px}
.logo-dot{width:30px;height:30px;border-radius:50%;background:var(--white)}
.nav a{position:absolute;top:40px;color:var(--white);font-family:"Oswald",sans-serif;font-size:13px;font-weight:500;text-decoration:none;text-transform:uppercase}
.hero-kicker{position:absolute;left:128px;top:176px;color:var(--white);font-family:"Oswald",sans-serif;font-weight:300;font-size:28px;letter-spacing:3px}
.hero-title{position:absolute;left:128px;top:204px;color:var(--white);font-family:"Oswald",sans-serif;font-weight:700;font-size:59px;line-height:62px;text-transform:uppercase}
.hero-rule{position:absolute;left:488px;top:426px;width:72px;height:2px;background:rgba(255,255,255,.5)}
.video-frame{position:absolute;left:550px;top:188px;width:585px;height:340px}

/* section headings */
.sec-title{position:absolute;left:0;width:1200px;text-align:center;font-family:"Oswald",sans-serif;font-weight:600;font-size:24px;color:var(--ink);text-transform:uppercase;z-index:2}
.sec-ghost{position:absolute;left:0;width:1200px;text-align:center;font-family:"Oswald",sans-serif;font-weight:700;font-size:84px;color:var(--ghost);text-transform:uppercase;letter-spacing:2px;z-index:1;line-height:1}
.sec-rule{position:absolute;left:582px;width:36px;height:2px;background:var(--ink);z-index:2}

/* services */
.services{position:absolute;left:130px;top:709px;width:953px;height:474px;display:grid;grid-template-columns:repeat(4,1fr);grid-template-rows:repeat(2,1fr);background:var(--white);box-shadow:0 4px 14px rgba(0,0,0,.08);z-index:2}
.service{position:relative;display:flex;flex-direction:column;align-items:center;padding-top:36px;border-right:1px solid var(--line);border-bottom:1px solid var(--line);text-align:center}
.service:nth-child(4n){border-right:none}
.service:nth-child(n+5){border-bottom:none}
.service svg{width:46px;height:46px;stroke:var(--blue);fill:none;stroke-width:2;stroke-linecap:round;stroke-linejoin:round}
.service h3{margin-top:22px;font-family:"Oswald",sans-serif;font-weight:600;font-size:15px;text-transform:uppercase;color:var(--ink)}
.service p{margin-top:10px;width:170px;font-size:10.5px;line-height:17px;color:var(--text)}
.service .more{position:relative;margin-top:14px;width:72px;height:21px;font-size:7px;box-shadow:none}
.service.featured{position:absolute;left:209px;top:-8px;width:272px;height:263px;background:var(--blue);box-shadow:0 10px 24px rgba(30,50,110,.35);border:none;z-index:3;padding-top:38px}
.service.featured svg{stroke:var(--white)}
.service.featured h3,.service.featured p{color:var(--white)}
.service.featured .more{width:92px;height:28px;font-size:9px}

/* newsletter */
.newsletter{position:absolute;left:0;top:1284px;width:1200px;height:451px;background:linear-gradient(120deg,#3b5aa8,#4a62aa)}
.newsletter-photo{position:absolute;left:0;top:0;width:604px;height:451px;background:linear-gradient(135deg,#5e6f86 0%,#b9c2cf 45%,#e8ebf0 65%,#8a7865 100%)}
.nl-kicker{position:absolute;left:660px;top:88px;color:var(--white);font-family:"Oswald",sans-serif;font-weight:300;font-size:26px;letter-spacing:3px}
.nl-title{position:absolute;left:660px;top:118px;color:var(--white);font-family:"Oswald",sans-serif;font-weight:700;font-size:54px;line-height:56px;text-transform:uppercase}
.field{position:absolute;background:var(--white);border-radius:3px;padding-left:14px;display:flex;align-items:center;font-family:"Oswald",sans-serif;font-weight:500;font-size:12px;color:var(--ink)}

/* testimonials */
.t-arrows{position:absolute;left:1080px;top:1880px;width:52px;height:24px}
.t-card{position:absolute;top:1930px;width:341px;height:173px;background:var(--white);box-shadow:0 3px 14px rgba(0,0,0,.09);padding:24px 26px}
.t-card.long{height:221px}
.t-head{display:flex;align-items:center;gap:14px}
.avatar{width:40px;height:40px;border-radius:50%;background:linear-gradient(135deg,#c9b9a6,#8fa0bb)}
.t-name{font-family:"Oswald",sans-serif;font-weight:600;font-size:13px;color:var(--blue)}
.t-role{font-size:8px;color:#9a9da4;margin-top:2px}
.t-body{margin-top:12px;font-size:8.5px;line-height:17px;color:var(--text)}
.t-quote{position:absolute;right:26px;bottom:6px;font-family:"Oswald",sans-serif;font-weight:700;font-size:44px;line-height:1;color:var(--orange)}

/* contact footer */
.footer-bg{position:absolute;left:0;top:2175px;width:1200px;height:700px}
.contact-title{position:absolute;left:0;top:2364px;width:1200px;text-align:center;color:var(--white);font-family:"Oswald",sans-serif;font-weight:600;font-size:24px;text-transform:uppercase}
.contact-rule{position:absolute;left:582px;top:2410px;width:36px;height:2px;background:var(--white)}
.label{position:absolute;color:var(--white);font-family:"Oswald",sans-serif;font-weight:500;font-size:12px}
.input{position:absolute;background:var(--white);border-radius:2px}
.send{position:absolute;left:792px;top:2678px;width:120px;height:31px;border:1.5px solid rgba(255,255,255,.85);border-radius:3px;color:var(--white);font-family:"Oswald",sans-serif;font-weight:500;font-size:10px;display:flex;align-items:center;justify-content:center;text-transform:uppercase}
.footer-info{position:absolute;left:0;top:2758px;width:1200px;display:flex;justify-content:center;align-items:center;gap:22px;color:var(--white);font-family:"Oswald",sans-serif;font-size:12px;font-weight:500}
.footer-mark{display:flex;align-items:center;gap:8px;font-weight:600;font-size:14px}
.footer-mark span{width:26px;height:26px;border-radius:50%;background:var(--white);display:block}
.footer-links{position:absolute;left:0;top:2810px;width:1200px;display:flex;justify-content:center;gap:24px;color:var(--white);font-family:"Oswald",sans-serif;font-size:9px;font-weight:500;text-transform:uppercase}
.footer-links i{font-style:normal;opacity:.7}
.footer-line{position:absolute;left:424px;top:2835px;width:548px;height:1px;background:rgba(255,255,255,.25)}
.copyright{position:absolute;left:0;top:2845px;width:1200px;text-align:center;color:var(--white);font-size:8px}
.social{position:absolute;top:2843px;width:15px;height:15px;border-radius:50%;border:1.5px solid var(--white)}
</style>
</head>
<body>

<header class="hero">
  <div class="abs" role="img" aria-label="Team meeting photo behind a blue overlay" style="inset:0;background:radial-gradient(ellipse at 30% 40%,rgba(120,140,190,.35),transparent 60%),radial-gradient(ellipse at 75% 60%,rgba(20,35,80,.35),transparent 60%)"></div>
  <svg class="hero-cut" width="1200" height="515" viewBox="0 0 1200 515"><polygon points="1082,0 1200,0 1200,292" fill="#fff"/></svg>
  <div class="logo"><span class="logo-dot"></span>YOURLOGO.COM</div>
  <nav class="nav">
    <a style="left:633px">Our Services</a>
    <a style="left:740px">Subscribe</a>
    <a style="left:830px">Testimonials</a>
  </nav>
  <div class="btn" style="left:943px;top:33px;width:113px;height:34px;font-size:13px">Get in touch</div>
  <div class="hero-kicker">DIGITAL MARKETING</div>
  <h1 class="hero-title">Be the best<br>with our team</h1>
  <div class="btn" style="left:130px;top:370px;width:152px;height:38px;font-size:14px">Get in touch</div>
  <div class="hero-rule"></div>
</header>

<svg class="video-frame" viewBox="0 0 585 340" role="img" aria-label="Laptop showing the homepage video of the team at work">
  <rect x="54" y="13" width="478" height="308" rx="14" fill="#1d1f26"/>
  <rect x="66" y="25" width="454" height="284" fill="#4d5f95"/>
  <circle cx="293" cy="167" r="30" fill="none" stroke="#fff" stroke-width="3"/>
  <polygon points="284,152 284,182 308,167" fill="#fff"/>
  <path d="M0 320 H585 L560 336 H25 Z" fill="#b9bcc4"/>
</svg>

<div class="sec-title" style="top:617px">Our services</div>
<div class="sec-rule" style="top:661px"></div>
<div class="sec-ghost" style="top:650px">Our services</div>

<section class="services">
  <div class="service">
    <svg viewBox="0 0 46 46"><circle cx="23" cy="18" r="12"/><polygon points="23,11 25,16 30,16 26,19 27.5,24 23,21 18.5,24 20,19 16,16 21,16"/><path d="M15 28 L11 42 L17 39 L20 44 L23 31 L26 44 L29 39 L35 42 L31 28"/></svg>
    <h3>PPC Champaign</h3>
    <p>Lorem ipsum dolor sit amet, consectetuer adipiscing elit. Aenean commodo ligula eget.</p>
    <div class="btn more">Read more</div>
  </div>
  <div class="service"></div>
  <div class="service">
    <svg viewBox="0 0 46 46"><rect x="6" y="32" width="6" height="10"/><rect x="16" y="26" width="6" height="16"/><rect x="26" y="20" width="6" height="22"/><rect x="36" y="14" width="6" height="28"/><path d="M6 24 L18 14 L26 18 L40 4 M32 4 H40 V12"/></svg>
    <h3>Lead generation</h3>
    <p>Lorem ipsum dolor sit amet, consectetuer adipiscing elit. Aenean commodo ligula eget.</p>
    <div class="btn more">Read more</div>
  </div>
  <div class="service">
    <svg viewBox="0 0 46 46"><rect x="4" y="5" width="38" height="36" rx="2"/><path d="M4 12 H42"/><circle cx="23" cy="27" r="10"/><path d="M13 27 H33 M23 17 C18 22 18 32 23 37 C28 32 28 22 23 17"/></svg>
    <h3>Web development</h3>
    <p>Lorem ipsum dolor sit amet, consectetuer adipiscing elit. Aenean commodo ligula eget.</p>
    <div class="btn more">Read more</div>
  </div>
  <div class="service">
    <svg viewBox="0 0 46 46"><path d="M30 8 H8 V42 H34 V24"/><path d="M14 18 H24 M14 25 H22 M14 32 H20"/><path d="M38 6 L42 10 L26 26 L20 28 L22 22 Z"/></svg>
    <h3>Content marketing</h3>
    <p>Lorem ipsum dolor sit amet, consectetuer adipiscing elit. Aenean commodo ligula eget.</p>
    <div class="btn more">Read more</div>
  </div>
  <div class="service">
    <svg viewBox="0 0 46 46"><rect x="4" y="6" width="36" height="28" rx="2"/><path d="M4 13 H40"/><circle cx="9" cy="9.5" r="1"/><circle cx="13" cy="9.5" r="1"/><path d="M26 42 V32 L34 25 L42 32 V42 Z"/></svg>
    <h3>Landing page optimization</h3>
    <p>Lorem ipsum dolor sit amet, consectetuer adipiscing elit. Aenean commodo ligula eget.</p>
    <div class="btn more">Read more</div>
  </div>
  <div class="service">
    <svg viewBox="0 0 46 46"><circle cx="18" cy="14" r="8"/><path d="M4 40 C4 30 10 24 18 24 C26 24 32 30 32 40 Z"/><path d="M26 7 C31 5 36 9 36 14 C36 19 32 22 28 22 M34 26 C39 28 42 33 42 40 H36"/></svg>
    <h3>Social media</h3>
    <p>Lorem ipsum dolor sit amet, consectetuer adipiscing elit. Aenean commodo ligula eget.</p>
    <div class="btn more">Read more</div>
  </div>
  <div class="service">
    <svg viewBox="0 0 46 46"><rect x="4" y="10" width="38" height="27" rx="1"/><path d="M4 10 L23 26 L42 10 M4 37 L18 22 M42 37 L28 22"/></svg>
    <h3>Email marketing</h3>
    <p>Lorem ipsum dolor sit amet, consectetuer adipiscing elit. Aenean commodo ligula eget.</p>
    <div class="btn more">Read more</div>
  </div>
  <div class="service featured">
    <svg viewBox="0 0 46 46"><path d="M18 28 C18 16 28 6 42 4 C40 18 30 28 18 28 Z"/><circle cx="32" cy="15" r="3.5"/><path d="M20 22 L10 20 L6 26 L16 28 M24 26 L26 36 L20 40 L18 30"/><path d="M14 32 L6 40 M10 30 L4 34 M16 36 L12 42"/></svg>
    <h3>Search optimization</h3>
    <p>Lorem ipsum dolor sit amet, consectetuer adipiscing elit. Aenean commodo ligula eget.</p>
    <div class="btn more">Read more</div>
  </div>
</section>

<section class="newsletter">
  <div class="newsletter-photo" role="img" aria-label="Hands on a laptop keyboard pointing at an analytics dashboard"></div>
  <div class="nl-kicker">NEWSLETTER SUBSCRIBE</div>
  <h2 class="nl-title">Subscribe now<br>happy hour</h2>
  <div class="field" style="left:660px;top:282px;width:230px;height:37px">Your Email</div>
  <div class="field" style="left:905px;top:282px;width:230px;height:37px">Company Name</div>
  <div class="btn" style="left:660px;top:340px;width:157px;height:36px;font-size:14px;text-transform:none">Sign up Now</div>
</section>

<div class="sec-title" style="top:1815px">What our clients say</div>
<div class="sec-rule" style="top:1859px"></div>
<div class="sec-ghost" style="top:1880px">Testimonials</div>
<svg class="t-arrows" viewBox="0 0 52 24"><path d="M22 12 H2 M9 5 L2 12 L9 19" stroke="#1b1b24" stroke-width="2" fill="none"/><path d="M30 12 H50 M43 5 L50 12 L43 19" stroke="#b5b8bf" stroke-width="2" fill="none"/></svg>

<article class="t-card" style="left:-116px">
  <div class="t-head"><div class="avatar" role="img" aria-label="Client portrait"></div><div><div class="t-name">Rowan Ellery</div><div class="t-role">CEO &amp; Owner / startup</div></div></div>
  <p class="t-body">Lorem ipsum dolor sit amet, consectetuer adipiscing elit. Aenean commodo ligula eget dolor. Aenean massa. Cum sociis natoque penatibus et magnis dis parturient montes, nascetur ridiculus mus.</p>
  <div class="t-quote">”</div>
</article>
<article class="t-card" style="left:245px">
  <div class="t-head"><div class="avatar" role="img" aria-label="Client portrait"></div><div><div class="t-name">Rowan Ellery</div><div class="t-role">CEO &amp; Owner / startup</div></div></div>
  <p class="t-body">Lorem ipsum dolor sit amet, consectetuer adipiscing elit. Aenean commodo ligula eget dolor. Aenean massa. Cum sociis natoque penatibus et magnis dis parturient montes, nascetur ridiculus mus. Donec quam felis, ultricies nec, pellentesque eu, pretium quis.</p>
  <div class="t-quote">”</div>
</article>
<article class="t-card long" style="left:606px">
  <div class="t-head"><div class="avatar" role="img" aria-label="Client portrait"></div><div><div class="t-name">Rowan Ellery</div><div class="t-role">CEO &amp; Owner / startup</div></div></div>
  <p class="t-body">Lorem ipsum dolor sit amet, consectetuer adipiscing elit. Aenean commodo ligula eget dolor. Aenean massa. Cum sociis natoque penatibus et magnis dis parturient montes, nascetur ridiculus mus. Donec quam felis, ultricies nec, pellentesque eu, pretium quis, sem. Nulla consequat massa quis enim. Donec pede justo, fringilla vel, aliquet nec, vulputate eget, arcu. In enim justo, rhoncus ut, imperdiet a, venenatis vitae, justo. Nullam dictum felis eu pede mollis.</p>
  <div class="t-quote">”</div>
</article>
<article class="t-card" style="left:968px">
  <div class="t-head"><div class="avatar" role="img" aria-label="Client portrait"></div><div><div class="t-name">Rowan Ellery</div><div class="t-role">CEO &amp; Owner / startup</div></div></div>
  <p class="t-body">Lorem ipsum dolor sit amet, consectetuer adipiscing elit. Aenean commodo ligula eget dolor. Aenean massa. Cum sociis natoque penatibus et magnis dis parturient montes, nascetur ridiculus mus. Donec quam felis, ultricies nec.</p>
  <div class="t-quote">”</div>
</article>

<svg class="footer-bg" viewBox="0 0 1200 700" preserveAspectRatio="none" role="img" aria-label="Blue background with a faint office photo">
  <defs><linearGradient id="fg" x1="0" y1="0" x2="1" y2="1"><stop offset="0" stop-color="#2f4b96"/><stop offset="1" stop-color="#4660ab"/></linearGradient></defs>
  <path d="M0 92 C220 70 420 62 620 58 C820 54 1000 30 1200 0 V700 H0 Z" fill="url(#fg)"/>
</svg>

<section>
  <h2 class="contact-title">Get in touch!</h2>
  <div class="contact-rule"></div>
  <div class="label" style="left:301px;top:2440px">Name</div>
  <div class="label" style="left:615px;top:2440px">Email Address</div>
  <div class="input" style="left:301px;top:2465px;width:299px;height:35px"></div>
  <div class="input" style="left:615px;top:2465px;width:297px;height:35px"></div>
  <div class="label" style="left:301px;top:2510px">Your Message</div>
  <div class="input" style="left:301px;top:2536px;width:611px;height:123px"></div>
  <div class="send">Send message</div>
</section>

<footer>
  <div class="footer-info">
    <span>hello@fernwick.example</span>
    <svg width="14" height="10" viewBox="0 0 14 10"><rect x="0.5" y="0.5" width="13" height="9" fill="#fff"/><path d="M0.5 0.5 L7 5.5 L13.5 0.5" stroke="#3b5aa8" fill="none"/></svg>
    <div class="footer-mark"><span></span>YOURLOGO</div>
    <span><svg width="11" height="11" viewBox="0 0 24 24" style="vertical-align:-1px;margin-right:6px"><path d="M6.6 10.8a15.1 15.1 0 006.6 6.6l2.2-2.2a1 1 0 011-.25 11.4 11.4 0 003.6.57 1 1 0 011 1V20a1 1 0 01-1 1A17 17 0 013 4a1 1 0 011-1h3.5a1 1 0 011 1c0 1.25.2 2.45.57 3.57a1 1 0 01-.25 1z" fill="#fff"/></svg>+370 600 123 45</span>
  </div>
  <div class="footer-links"><span>Our services</span><i>|</i><span>Subscribe</span><i>|</i><span>Testimonials</span><i>|</i><span>Get in touch</span></div>
  <div class="footer-line"></div>
  <div class="copyright">Copyright 2018 Domain All rights reserved</div>
  <div class="social" style="left:918px"></div>
  <div class="social" style="left:937px"></div>
  <div class="social" style="left:956px"></div>
</footer>

</body>
</html>
```